Business Card for Brevikpartners

Need to design a business card with attached logo

Target Market(s)

I'm a financial/Investment adviser so card must be professional

Industry/Entity Type

Business

Font styles to use
Serif
Sans Serif

Requirements
Must have
• Would like in include the GOLD version of my logo if possible

Teddy Brevik
President

Address is
4817 Pellingham Blvd
Dunmore, Ca. 94712

Phone
510-374-9182
Fax
925-463-7208

Email
teddy@brevikpartners.example

I also need the following tag line at the bottom of card:

Investment Advisor Representative of and Securities offered
through Harborview Capital Securities, LLC Member QMTRA, DEWB
and Registered Investment Advisor.

Nice to have
• Split color in order to incorporate GOLD LOGO
Should not have

```html
<!DOCTYPE html>
<html lang="en">
<head>
<meta charset="utf-8">
<title>Brevik Partners – Business Card</title>
<link rel="stylesheet" href="https://fonts.googleapis.com/css2?family=Cinzel:wght@400;600&family=Ubuntu:wght@400&family=Mulish:wght@600&display=swap">
<style>
  :root {
    --page-bg: #2a2622;
    --card-black: #000000;
    --gold: #d9b24a;
    --gold-deep: #c59a2c;
    --gold-bright: #fcd25a;
    --gold-pale: #fff9dc;
    --muted-beige: #e6e0d2;
    --white: #ffffff;
    --ink: #000000;
  }
  * { margin: 0; padding: 0; box-sizing: border-box; }
  html, body {
    width: 1200px; height: 1000px; overflow: hidden;
    background: var(--page-bg);
  }
  .business-card {
    position: absolute;
    left: 242px; top: 262px;
    width: 716px; height: 477px;
    background: var(--card-black);
    overflow: hidden;
  }
  .gold-wave {
    position: absolute; left: 0; top: 0;
    width: 716px; height: 477px;
  }
  .brand {
    position: absolute;
    left: 44px; top: 96px;
    display: flex; align-items: center; gap: 8px;
  }
  .brand-dot {
    width: 14px; height: 14px; border-radius: 50%;
    background: var(--gold);
  }
  .brand-name {
    font-family: "Cinzel", serif;
    font-weight: 400;
    font-size: 17px;
    color: var(--gold);
    letter-spacing: 0.5px;
  }
  .disclosure {
    position: absolute;
    left: 252px; top: 24px;
    font-family: "Ubuntu", sans-serif;
    font-size: 13.6px;
    line-height: 17.5px;
    color: var(--white);
  }
  .advisor {
    position: absolute;
    left: 0; width: 716px; top: 170px;
    text-align: center;
  }
  .advisor-name {
    font-family: "Cinzel", serif;
    font-weight: 600;
    font-size: 27px;
    color: var(--gold);
    line-height: 34px;
  }
  .advisor-title {
    font-family: "Cinzel", serif;
    font-weight: 400;
    font-size: 16px;
    letter-spacing: 1px;
    color: var(--muted-beige);
    line-height: 22px;
  }
  .contact {
    position: absolute;
    left: 36px; top: 326px;
    font-family: "Mulish", sans-serif;
    font-weight: 600;
    font-size: 16px;
    line-height: 21px;
    color: var(--ink);
  }
  .contact-row { display: flex; }
  .contact-label { width: 82px; }
</style>
</head>
<body>
  <div class="business-card">
    <svg class="gold-wave" viewBox="0 0 716 477" aria-hidden="true">
      <defs>
        <linearGradient id="goldFill" x1="0" y1="0" x2="0" y2="1">
          <stop offset="0" stop-color="#fcd25a"/>
          <stop offset="0.45" stop-color="#fff9dc"/>
          <stop offset="0.75" stop-color="#f1dc9a"/>
          <stop offset="1" stop-color="#c59a2c"/>
        </linearGradient>
      </defs>
      <path d="M0 282 C 70 268, 160 266, 270 282 C 420 304, 560 352, 716 372 V477 H0 Z"
            fill="url(#goldFill)"/>
    </svg>

    <div class="brand">
      <span class="brand-dot"></span>
      <span class="brand-name">Brevik Partners</span>
    </div>

    <p class="disclosure">
      Investment Advisor Representative of and Securities offered<br>
      through Harborview Capital Securities, LLC Member QMTRA, DEWB<br>
      and Registered Investment Advisor
    </p>

    <div class="advisor">
      <h1 class="advisor-name">TEDDY BREVIK</h1>
      <p class="advisor-title">PRESIDENT</p>
    </div>

    <div class="contact">
      <div class="contact-row"><span class="contact-label">Address :</span><span>4817 Pellingham Blvd</span></div>
      <div class="contact-row"><span class="contact-label"></span><span>Dunmore, Ca. 94712</span></div>
      <div class="contact-row"><span class="contact-label">Phone:</span><span>510-374-9182</span></div>
      <div class="contact-row"><span class="contact-label">Fax:</span><span>925-463-7208</span></div>
      <div class="contact-row"><span class="contact-label">Email:</span><span>teddy@brevikpartners.example</span></div>
    </div>
  </div>
</body>
</html>
```